Business Card Design Project

I need the following:

Logo -
Name - Dale Prewitt
Title - Customer Experience Officer
Web - www.bvrh.net
Phone - 555-417-3068
Updates

Project Deadline Extended
Reason: I launched the project later than anticipated. I look forward to seeing your designs. Dale

Industry/Entity Type

Business

```html
<!DOCTYPE html>
<html lang="en">
<head>
<meta charset="utf-8">
<title>Beacon Vale Relay Hub – Business Cards</title>
<link rel="stylesheet" href="https://fonts.googleapis.com/css2?family=Open+Sans:wght@400;600;700&display=swap">
<style>
  :root {
    --stage: #ecebe8;
    --card-light: #ffffff;
    --card-shade: #e2e3e5;
    --brand-blue: #0e62a3;
    --brand-blue-light: #2597d6;
    --band-black: #111111;
    --ink: #1c1c1c;
    --ink-soft: #4a4a4a;
    --on-blue: #ffffff;
  }
  * { box-sizing: border-box; margin: 0; padding: 0; }
  html, body {
    width: 1200px; height: 899px; overflow: hidden;
    background: var(--stage);
    font-family: "Open Sans", Arial, sans-serif;
  }
  .stage {
    position: relative; width: 1200px; height: 899px;
    display: flex; flex-direction: column; align-items: center; justify-content: center; gap: 56px;
  }
  .card {
    position: relative; width: 600px; height: 343px; overflow: hidden;
    background: radial-gradient(ellipse at 60% 55%, var(--card-light) 0%, var(--card-shade) 100%);
    box-shadow: 0 6px 18px rgba(0,0,0,.18);
  }
  .card__swoosh { position: absolute; inset: 0; width: 100%; height: 100%; }
  .brand { position: absolute; display: flex; align-items: center; gap: 14px; }
  .brand__dot {
    width: 72px; height: 72px; border-radius: 50%;
    background: var(--brand-blue); flex: none;
  }
  .brand__name {
    font-weight: 700; font-size: 23px; line-height: 1.02; letter-spacing: .5px;
    text-transform: uppercase; color: var(--ink);
  }
  .brand__web {
    display: block; margin-top: 6px; padding-top: 3px;
    border-top: 1.5px solid var(--brand-blue-light);
    font-size: 10px; font-weight: 600; color: var(--brand-blue); text-align: center;
  }
  .card--front .brand { left: 54px; top: 176px; }

  .holder { position: absolute; left: 22px; top: 26px; color: var(--on-blue); }
  .holder__name { font-size: 23px; font-weight: 600; }
  .holder__title { font-size: 16px; margin-top: 6px; white-space: nowrap; }
  .card--back .brand { left: 150px; top: 160px; }
  .card--back .brand__dot { width: 62px; height: 62px; }
  .card--back .brand__name { font-size: 20px; }

  .contact {
    position: absolute; right: 24px; top: 168px; list-style: none;
    font-size: 13px; color: var(--ink-soft); text-align: right; line-height: 21px;
  }
  .contact li { display: flex; justify-content: flex-end; align-items: center; gap: 7px; }
  .contact svg { width: 14px; height: 14px; fill: none; stroke: var(--brand-blue-light); stroke-width: 1.6; }
  .address {
    position: absolute; left: 22px; bottom: 22px;
    font-size: 13px; color: var(--ink-soft); line-height: 19px; font-style: normal;
  }
</style>
</head>
<body>
<main class="stage">

  <section class="card card--front" aria-label="Card front">
    <svg class="card__swoosh" viewBox="0 0 600 343" preserveAspectRatio="none" aria-hidden="true">
      <defs>
        <linearGradient id="blueFront" x1="0" y1="0" x2="1" y2="0">
          <stop offset="0" stop-color="var(--brand-blue)"/>
          <stop offset=".55" stop-color="var(--brand-blue-light)"/>
          <stop offset="1" stop-color="var(--brand-blue)"/>
        </linearGradient>
      </defs>
      <path d="M0 0 H600 V68 C400 70 170 95 0 162 Z" fill="var(--band-black)"/>
      <path d="M0 0 H600 V57 C400 58 170 82 0 148 Z" fill="#ffffff"/>
      <path d="M0 0 H600 V52 C400 52 170 76 0 142 Z" fill="url(#blueFront)"/>
    </svg>
    <div class="brand">
      <span class="brand__dot"></span>
      <div>
        <div class="brand__name">Beacon Vale<br>Relay Hub</div>
        <span class="brand__web">www.bvrh.net</span>
      </div>
    </div>
  </section>

  <section class="card card--back" aria-label="Card back">
    <svg class="card__swoosh" viewBox="0 0 600 343" preserveAspectRatio="none" aria-hidden="true">
      <defs>
        <linearGradient id="blueBack" x1="0" y1="0" x2="1" y2="1">
          <stop offset="0" stop-color="var(--brand-blue)"/>
          <stop offset=".6" stop-color="var(--brand-blue-light)"/>
          <stop offset="1" stop-color="var(--brand-blue)"/>
        </linearGradient>
      </defs>
      <path d="M0 0 H600 V68 C380 70 110 130 0 292 Z" fill="var(--band-black)"/>
      <path d="M0 0 H600 V56 C380 58 105 118 0 278 Z" fill="#ffffff"/>
      <path d="M0 0 H600 V51 C380 52 100 112 0 272 Z" fill="url(#blueBack)"/>
    </svg>
    <div class="holder">
      <div class="holder__name">Dale Prewitt</div>
      <div class="holder__title">Customer Experience Officer</div>
    </div>
    <div class="brand">
      <span class="brand__dot"></span>
      <div>
        <div class="brand__name">Beacon Vale<br>Relay Hub</div>
        <span class="brand__web">www.bvrh.net</span>
      </div>
    </div>
    <ul class="contact">
      <li>555.417.3068 <svg viewBox="0 0 16 16"><path d="M3 2h3l1.5 3.5-2 1.3a8 8 0 0 0 3.7 3.7l1.3-2L14 10v3a1.5 1.5 0 0 1-1.5 1.5A11 11 0 0 1 1.5 3.5 1.5 1.5 0 0 1 3 2z"/></svg></li>
      <li>555.417.3068 <svg viewBox="0 0 16 16"><rect x="4.5" y="1.5" width="7" height="13" rx="1.2"/><path d="M7 12.5h2"/></svg></li>
      <li>info@bvrh.net <svg viewBox="0 0 16 16"><rect x="1.5" y="3.5" width="13" height="9"/><path d="M1.5 3.5 8 9l6.5-5.5"/></svg></li>
      <li>www.bvrh.net <svg viewBox="0 0 16 16"><circle cx="8" cy="8" r="6.5"/><path d="M1.5 8h13M8 1.5c-3 3.5-3 9.5 0 13M8 1.5c3 3.5 3 9.5 0 13"/></svg></li>
    </ul>
    <address class="address">0418 W. Alder Street, Suite 310<br>Fairview, OR 97024</address>
  </section>

</main>
</body>
</html>
```